Business Card for a Child Psychologist

I am a psychologist working with children and families and need a business card to give to clients and referral sources. I see children of all ages, so it should not look too young - as it will be for older children too. My work involves dealing with families in difficult situations, likes divorce, or with issues such as depression and anxiety. The design should communicate that I provide an open,warm, friendly, and caring atmosphere. I want to convey a sense of hope and positivity. Using colors like blues, purples

Target Market(s)

Families, doctors, family law attorneys

Industry/Entity Type

Psychology

Contact Information for Business Card

Lorna Pettigrew, Ph.D.
462 W. Brambleton, Suite 2150
Chicago, Illinois 60688
312-555-0173
drlornampettigrew@quenmail.example

Font styles to use
Script

Requirements
Must have
• A Logo to go with the details of my contact information.
Should not have
• Nothing in the shape of a brain. Nothing sad, or that looks too clinical.

```html
<!DOCTYPE html>
<html lang="en">
<head>
<meta charset="utf-8">
<title>Lorna Pettigrew, Ph.D. – Business Card</title>
<link rel="stylesheet" href="https://fonts.googleapis.com/css2?family=Pinyon+Script&family=Josefin+Sans:wght@300&display=swap">
<style>
  :root {
    --page-bg: #ededed;
    --card-top: #e2d6fb;
    --card-bottom: #ddd2f8;
    --ink: #6e5f86;
    --blue: #3aa3e3;
    --violet: #b89af2;
    --royal: #5786f0;
  }
  * { box-sizing: border-box; margin: 0; padding: 0; }
  html, body {
    width: 1200px; height: 882px; overflow: hidden;
    background: var(--page-bg);
  }
  body { display: flex; align-items: center; justify-content: center; }
  .business-card {
    position: relative;
    width: 1000px; height: 572px;
    overflow: hidden;
    background: linear-gradient(160deg, var(--card-top), var(--card-bottom));
    box-shadow: 0 10px 30px rgba(0,0,0,0.12);
  }
  .contact {
    position: absolute; left: 110px; top: 80px;
    width: 560px;
    color: var(--ink);
    font-family: "Josefin Sans", sans-serif;
    font-style: normal;
    font-weight: 300; font-size: 26px; line-height: 1.3;
    white-space: nowrap;
  }
  .contact .name {
    font-family: "Pinyon Script", cursive;
    font-weight: 400; font-size: 40px; line-height: 1.15;
    margin-bottom: 4px;
  }
  .heart-logo-area {
    position: absolute; left: 700px; top: 270px;
    width: 250px; height: 302px;
    border-radius: 40px 40px 0 0;
    background: linear-gradient(160deg, var(--blue) 0%, var(--violet) 50%, var(--royal) 100%);
  }
</style>
</head>
<body>
  <main class="business-card">
    <address class="contact">
      <p class="name">Lorna Pettigrew, Ph.D.</p>
      <p class="street">462 W. Brambleton, Suite 2150</p>
      <p class="city">Chicago, Illinois 60688</p>
      <p class="phone">Tel: 312-555-0173</p>
      <p class="email">Email: drlornampettigrew@quenmail.example</p>
    </address>
    <div class="heart-logo-area" role="img" aria-label="Heart made of blue and purple interlocking puzzle pieces, with one piece lifted at the top"></div>
  </main>
</body>
</html>
```